Property Developer - Simple yet Sophisticated and Sharp Business Card

We are a medium sized property developer involved mainly in townhouse developments and land subdivisions.

The company is looking for a simple, sharp and sophisticated business card that will be given to contractors, land owners, financiers etc and thus will need to look professional.

Property development related graphics and art can be used, however the card is not to be too "busy" or crowded. Our company name is KL Estates which could possibly be incorporated into the graphics or artwork.

Single sided and/or double sided designs will be acceptable.

A Simple, Sophisticated, Sharp design please!

Good Luck !

```html
<!DOCTYPE html>
<html lang="en">
<head>
<meta charset="utf-8">
<title>KL Estates – Business Card</title>
<link rel="stylesheet" href="https://fonts.googleapis.com/css2?family=Russo+One&family=Roboto+Condensed:wght@700&display=swap">
<style>
  :root {
    --backdrop: #d9d9d9;
    --card-centre: #444444;
    --card-edge: #1f1f1f;
    --band-green: #6aa84f;
    --band-green-light: #7dbb5e;
    --label-green: #5a8a3c;
    --band-text: #ececec;
    --contact-text: #f4f4f4;
  }
  * { box-sizing: border-box; }
  html, body {
    margin: 0;
    width: 1200px;
    height: 900px;
    overflow: hidden;
    background: var(--backdrop);
  }
  .sheet {
    position: relative;
    width: 1200px;
    height: 900px;
  }
  .card {
    position: absolute;
    top: 100px;
    width: 420px;
    height: 700px;
    overflow: hidden;
    background: radial-gradient(ellipse at 55% 45%, var(--card-centre) 0%, #333 45%, var(--card-edge) 100%);
    box-shadow: 0 10px 30px rgba(0, 0, 0, 0.35);
  }
  .card--front { left: 140px; }
  .card--back { left: 640px; }

  .fold {
    position: absolute;
    inset: 0;
    width: 420px;
    height: 700px;
    pointer-events: none;
  }

  .holder-name {
    position: absolute;
    top: 150px;
    left: 0;
    width: 420px;
    text-align: center;
    margin: 0;
    font-family: "Russo One", sans-serif;
    font-size: 30px;
    letter-spacing: 1px;
    color: var(--label-green);
  }

  .band {
    position: absolute;
    background: linear-gradient(90deg, var(--band-green) 0%, var(--band-green-light) 50%, var(--band-green) 100%);
    box-shadow: 6px 8px 14px rgba(0, 0, 0, 0.45);
    display: flex;
    align-items: center;
    justify-content: center;
  }
  .band--name {
    left: 200px;
    top: 240px;
    width: 104px;
    height: 440px;
  }
  .band__title {
    writing-mode: vertical-rl;
    font-family: "Russo One", sans-serif;
    font-size: 54px;
    letter-spacing: 2px;
    color: var(--band-text);
    margin: 0;
  }

  .company-label {
    position: absolute;
    top: 58px;
    left: 170px;
    margin: 0;
    font-family: "Russo One", sans-serif;
    font-size: 34px;
    line-height: 40px;
    letter-spacing: 1px;
    color: var(--label-green);
    transform: rotate(31deg);
    transform-origin: left top;
    white-space: nowrap;
  }

  .band--contact {
    left: 150px;
    top: 215px;
    width: 116px;
    height: 315px;
    padding: 12px 8px;
  }
  .contact {
    writing-mode: vertical-rl;
    margin: 0;
    padding: 0;
    list-style: none;
    font-family: "Roboto Condensed", sans-serif;
    font-weight: 700;
    font-size: 13px;
    line-height: 24px;
    color: var(--contact-text);
    text-transform: uppercase;
    height: 100%;
    text-align: end;
    white-space: nowrap;
  }

  .band--mark {
    left: 128px;
    top: 560px;
    width: 132px;
    height: 130px;
  }
  .mark {
    writing-mode: vertical-rl;
    font-family: "Russo One", sans-serif;
    font-size: 72px;
    line-height: 1;
    color: var(--band-text);
    margin: 0;
  }
</style>
</head>
<body>
<main class="sheet">

  <section class="card card--front" aria-label="Business card front">
    <p class="holder-name">YOUR NAME</p>
    <div class="band band--name">
      <h1 class="band__title">KL ESTATES</h1>
    </div>
    <svg class="fold" viewBox="0 0 420 700" aria-hidden="true">
      <defs>
        <linearGradient id="front-fold" x1="0" y1="0" x2="0" y2="1">
          <stop offset="0" stop-color="#ffffff" stop-opacity="0.08"/>
          <stop offset="1" stop-color="#ffffff" stop-opacity="0"/>
        </linearGradient>
      </defs>
      <polygon points="100,190 420,260 420,200 100,160" fill="url(#front-fold)"/>
      <line x1="100" y1="190" x2="420" y2="260" stroke="rgba(0,0,0,0.35)" stroke-width="3"/>
    </svg>
  </section>

  <section class="card card--back" aria-label="Business card back">
    <svg class="fold" viewBox="0 0 420 700" aria-hidden="true">
      <defs>
        <linearGradient id="back-fold" x1="0" y1="1" x2="0.4" y2="0">
          <stop offset="0" stop-color="#ffffff" stop-opacity="0.10"/>
          <stop offset="1" stop-color="#ffffff" stop-opacity="0"/>
        </linearGradient>
      </defs>
      <polygon points="120,110 420,290 420,150 180,40" fill="url(#back-fold)"/>
      <line x1="120" y1="110" x2="420" y2="290" stroke="rgba(0,0,0,0.35)" stroke-width="3"/>
    </svg>
    <p class="company-label">KL ESTATES</p>
    <div class="band band--contact">
      <ul class="contact">
        <li>Phone: (07) 3000 4812</li>
        <li>Fax: (07) 3000 4813</li>
        <li>Email: projects@klestates-mail.com</li>
        <li>Postal: PO Box 2208 Elmvale QLD 4000</li>
      </ul>
    </div>
    <div class="band band--mark">
      <p class="mark">KL</p>
    </div>
  </section>

</main>
</body>
</html>
```